Book cover for a book about how to support a friend in grief.

The title of the book is "Quiet Hands on Heavy Days: Standing Beside Someone Across Hard Seasons" by Daniel P. Hartwig. I am a grief counselor and am passionate about educating people on how to better support someone in grief. I'd like the cover to tell a story. Maybe a person in grief and a friend standing near who doesn't know what to say. The image should appeal to all genders. I am open to ANY other ideas for the cover. Grief is a heavy topic but I don't want the cover to feel sad. It should convey hope.

```html
<!DOCTYPE html>
<html lang="en">
<head>
<meta charset="utf-8">
<title>Quiet Hands on Heavy Days — Book Cover</title>
<link rel="stylesheet" href="https://fonts.googleapis.com/css2?family=Amatic+SC:wght@700&family=Rubik+Mono+One&family=Cabin+Sketch:wght@700&family=Oswald:wght@600&display=swap">
<style>
  :root {
    --backdrop: #8a8a8a;
    --cover-black: #0c0c0c;
    --blush: #ecd8dc;
    --paper: #ececec;
    --paper-shade: #dcdcdc;
    --ink: #111111;
    --line-white: #f4f4f4;
  }
  * { margin: 0; padding: 0; box-sizing: border-box; }
  html, body {
    width: 1200px;
    height: 960px;
    overflow: hidden;
    background: var(--backdrop);
  }
  .canvas {
    position: relative;
    width: 1200px;
    height: 960px;
  }
  .cover {
    position: absolute;
    left: 300px;
    top: 50px;
    width: 600px;
    height: 860px;
    background: var(--cover-black);
    overflow: hidden;
  }
  .title {
    position: absolute;
    left: 96px;
    top: 92px;
    color: var(--blush);
    font-family: "Amatic SC", cursive;
    font-weight: 700;
    line-height: 0.95;
    text-transform: uppercase;
  }
  .title-line { display: block; white-space: nowrap; }
  .title-line--1 { font-size: 88px; margin-left: 0; }
  .title-line--2 { font-size: 58px; margin-left: 70px; }
  .title-line--3 { font-size: 62px; margin-left: 40px; }
  .title-line--4 { font-size: 88px; margin-left: 60px; }
  .accent-block {
    font-family: "Rubik Mono One", sans-serif;
    font-size: 0.62em;
  }
  .accent-sketch {
    font-family: "Cabin Sketch", cursive;
    font-weight: 700;
    font-size: 0.8em;
  }
  .thought-cloud {
    position: absolute;
    left: 370px;
    top: 150px;
    width: 180px;
    height: 140px;
  }
  .friends-illustration {
    position: absolute;
    left: 70px;
    top: 400px;
    width: 500px;
    height: 460px;
    background: linear-gradient(180deg, var(--paper) 0%, var(--paper-shade) 100%);
    border-radius: 250px 250px 0 0;
  }
  .subtitle {
    position: absolute;
    left: 190px;
    top: 445px;
    color: var(--ink);
    font-family: "Amatic SC", cursive;
    font-weight: 700;
    line-height: 0.92;
    text-transform: uppercase;
  }
  .subtitle-line { display: block; white-space: nowrap; font-size: 50px; }
  .subtitle-line--2 { margin-left: 18px; }
  .subtitle-line--3 { margin-left: 6px; }
  .subtitle-line--5 { margin-left: 60px; }
  .author {
    position: absolute;
    left: 200px;
    top: 712px;
    color: var(--ink);
    font-family: "Oswald", sans-serif;
    font-weight: 600;
    font-size: 24px;
    letter-spacing: 1px;
    text-transform: uppercase;
  }
</style>
</head>
<body>
<main class="canvas">
  <section class="cover">
    <h1 class="title">
      <span class="title-line title-line--1">Qui<span class="accent-block">e</span>t</span>
      <span class="title-line title-line--2">Ha<span class="accent-sketch">n</span>ds on</span>
      <span class="title-line title-line--3"><span class="accent-block">H</span>eavy</span>
      <span class="title-line title-line--4">D<span class="accent-sketch">a</span>ys</span>
    </h1>

    <svg class="thought-cloud" viewBox="0 0 180 140" aria-hidden="true">
      <path d="M40 95 C15 95 10 65 32 58 C22 35 50 20 66 34 C74 12 108 10 116 30 C136 16 166 32 156 56 C178 66 170 98 146 96 C146 116 120 122 108 108 C96 124 68 122 64 106 C56 112 38 110 40 95 Z"
            fill="none" stroke="var(--line-white)" stroke-width="5" stroke-linejoin="round"/>
      <circle cx="22" cy="124" r="6" fill="none" stroke="var(--line-white)" stroke-width="4"/>
    </svg>

    <div class="friends-illustration" role="img"
         aria-label="White silhouette of a thoughtful friend in profile, with a small dark figure of a grieving person sitting within it"></div>

    <p class="subtitle">
      <span class="subtitle-line subtitle-line--1">Standing</span>
      <span class="subtitle-line subtitle-line--2">Beside</span>
      <span class="subtitle-line subtitle-line--3">Someone</span>
      <span class="subtitle-line subtitle-line--4">Across Hard</span>
      <span class="subtitle-line subtitle-line--5">Seasons</span>
    </p>

    <p class="author">– Daniel P. Hartwig</p>
  </section>
</main>
</body>
</html>
```